Wordpress Design Project

WHO WE ARE:
Bright Path Web Growth is not just another SEO or PPC company. We work with our clients to help them grow their business and achieve their goals. Our commitment to doing what is best for the customer, is why we have grown so quickly. We believe our business is not about advertising BUT about connecting customers & growing our clients businesses. We see our product as helping people, not selling a product.

PROJECT OVERVIEW:
I need to create a wordpress website for my business, www.brightpathwebgrowth.com.au

I need a whole new site created showing all of my services. The services include:
NOTE: These are not the main focus of the home page.

Consulting & Strategy Planning
Search Engine Optimisation
Pay Per Click
Re-Marketing

Once I have selected the top home page design, I will need a product and blog page designed.

SITE DESIGN:
If I was to explain the kind of style I am looking for, it would be high-street, New York agency look, web 2.0. Clean, elegant, stylish, high quality and simple looking. Kind of like you would expect from an quince website.

Think of car advertising, the closest to the target market & look/feel Im looking for would be Ravenmotor, Korel, Tamar, Brandin, Zepra.

However, I am open to any design style.

DO NOT let this restrict your creativity BUT here are some websites I like the look of.

Home page:
http://www.layoutfoundry.example/demo/52816.html
https://www.vantorix.example/intl/en/halo/devices/
http://www.vantorix.example/intl/en/halo/devices/features-different.html
http://www.layoutfoundry.example/demo/47190.html
https://www.vantorix.example/intl/en/halo/browser/features.html

Product Page:
http://www.vantorix.example/intl/en/halo/devices/buynow.html#instore

NOTE: I just added a file called "I like this color scheme.png" you can play around with something like this as well.
Updates

Please do not use the content from my current website. That is for a PPC service, the new site is for an full service agency.

Also, the message/tagline is the feature or most prominent element of the website..... Not the services we offer, these are secondary.

Great designs so far everyone, but I think I'm looking a little simpler and less crowded.  Closer to the sample sites I sent.... keep em coming.

Also, I would prefer that the 4 services, do not visually over power the tag line.  The 4 services are not important to the home page.

Lets make this easy, since every design I receive is almost the same...

Make the design look something like these 2 websites.
https://www.vantorix.example/intl/en/halo/browser/features.html#simplicity

Target Market(s)

Business Owners and entreprenuers who are well established, typically in the 35-60 year old range and spend 100k-1m in advertising per year. They big brands that target these people are Ravenmotor, Korel, Tamar, Brandin, Zepra, this should give you the feel for what I am after.

Industry/Entity Type

Advertising

Requirements
Must have
• 1. Navigations: Home, Services, About Us, Blog, Contact Us

2. The main home page words should be.... "We Grow Your Business Online" and "Clear Aim, Clear Plan, Clear Team, Bright Path Web Growth" (should use logo for last one)
I would like to see this tagline somewhere in the site "We Don't Want to be the Biggest, Just the Best!"

3. Product page must have a contact form with (name, email, phone, website)
This form must show an offer of "Free Strategy Sessions, Double your website leads", I have included an image to show as an example for the lead form "lead form example.png", see attached.

Nice to have
• I would like to see 1 or 2 of these idea's in the design.

1. I have attached some logos for Bidlane & Metricove certifications + Web association logo you can use for design purposes.

2. You can put company logo's in the design and I can change them to my clients logos at a later date.

3. Testimonials

4. Since our business is about people, pictures of people like business owners, customers using technology such as an slate, or anything like that would be good. However, is not necessary. Some idea: http://www.peerlattice.example/advertising
Should not have
• There will be no video on the design.

```html
<!DOCTYPE html>
<html lang="en">
<head>
<meta charset="utf-8">
<title>Bright Path Web Growth</title>
<link rel="stylesheet" href="https://fonts.googleapis.com/css2?family=Fredoka:wght@600&family=Ubuntu:wght@400;500;700&family=Gelasio:ital@0;1&display=swap">
<style>
:root{
  --blue:#3a9be0;
  --blue-deep:#1e6fc8;
  --link:#1f67b8;
  --orange:#f08a1e;
  --orange-deep:#e4560c;
  --ink:#1c1c1c;
  --text:#333;
  --muted:#555;
  --rule:#d6d6d6;
  --band:#f2f2f2;
  --page:#fff;
}
*{box-sizing:border-box;margin:0;padding:0}
html,body{width:983px;height:1200px;overflow:hidden;background:var(--page)}
body{position:relative;font-family:"Ubuntu",sans-serif;color:var(--text)}

/* header */
.site-header{position:absolute;left:0;top:0;width:983px;height:91px;background:linear-gradient(#fff,#f3f3f3);border-bottom:1px solid #dcdcdc}
.brand{position:absolute;left:116px;top:22px;display:flex;align-items:center;gap:12px}
.brand-mark{width:40px;height:40px;border-radius:50%;background:var(--blue-deep)}
.brand-name{font-family:"Ubuntu",sans-serif;font-weight:700;font-size:24px;color:#333;letter-spacing:-.3px}
.share{position:absolute;top:18px;display:flex;gap:8px;right:116px}
.share span{display:block;height:15px;border:1px solid #c8c8c8;border-radius:2px;background:linear-gradient(#fff,#e9e9e9);font-size:9px;line-height:13px;padding:0 5px;color:#333}
.main-nav{position:absolute;top:51px;right:116px;display:flex;align-items:center}
.main-nav a{font-size:11px;font-weight:500;color:#555;text-decoration:none;text-transform:uppercase;margin-left:46px}
.main-nav a.current{color:var(--blue-deep)}

/* hero */
.hero{position:absolute;left:0;top:92px;width:983px;height:408px;background:radial-gradient(ellipse at 45% 30%,#fff 0,#fff 40%,#eef5fc 70%,#fafcff 100%);overflow:hidden}
.hero-photo{position:absolute;z-index:1;left:525px;top:23px;width:338px;height:385px;background:linear-gradient(180deg,#f1e5da 0,#d8b9a0 30%,#f4f4f4 55%,#2d3543 62%,#1e2430 100%);border-radius:120px 120px 0 0}
.hero-title{position:absolute;z-index:2;left:115px;top:38px;font-family:"Fredoka",sans-serif;font-weight:600;font-size:25.5px;line-height:31px;color:var(--blue);text-transform:uppercase;letter-spacing:0;white-space:nowrap}
.hero-title .accent{color:var(--orange)}
.hero-copy{position:absolute;z-index:2;left:118px;top:184px;width:410px;font-family:"Gelasio",serif;font-style:italic;font-size:13.2px;line-height:20.5px;color:#222}
.btn-more{position:absolute;z-index:2;left:115px;top:273px;width:97px;height:28px;border:1px solid #c9c9c9;border-radius:3px;background:linear-gradient(#fff,#e6e6e6);font-size:12px;font-weight:500;color:#222;display:flex;align-items:center;justify-content:center;gap:5px}
.slider-bar{position:absolute;z-index:2;left:115px;top:342px;width:390px;height:38px;border-radius:4px 0 0 4px;background:linear-gradient(90deg,#e6e6e6,#eeeeee 60%,rgba(240,240,240,0))}
.dots{position:absolute;left:15px;top:14px;display:flex;gap:4px}
.dots i{width:11px;height:11px;border-radius:50%;background:#d4d4d4}
.dots i.on{background:#333}
.arrows{position:absolute;left:92px;top:11px;font-size:12px;color:#666;letter-spacing:4px}

/* services */
.services{position:absolute;left:0;top:500px;width:983px;height:163px;background:var(--band);border-top:1px solid #e2e2e2;border-bottom:1px solid #e2e2e2}
.service{position:absolute;top:22px;width:160px}
.service-head{display:flex;align-items:center;gap:8px;height:40px}
.service-head h3{font-family:"Ubuntu",sans-serif;font-weight:500;font-size:14.5px;line-height:20px;color:var(--ink);white-space:nowrap}
.service p{margin-top:14px;font-size:10px;line-height:14px;color:#222}
.service a{display:block;margin-top:13px;font-size:10px;font-weight:500;color:var(--link);text-decoration:none}

/* testimonials */
.says-title{position:absolute;left:118px;top:692px;font-weight:500;font-size:14.5px;color:var(--ink)}
.quote{position:absolute;top:734px;width:162px;height:230px}
.quote .mark{position:absolute;left:-24px;top:0}
.quote p{font-family:"Gelasio",serif;font-style:italic;font-size:10px;line-height:16.8px;color:#444;margin-bottom:16px}
.quote .who{position:absolute;top:191px;font-size:11px;font-weight:500;color:var(--ink)}
.quote .site{position:absolute;top:209px;font-family:"Gelasio",serif;font-size:10px;color:#555;white-space:nowrap}

/* lead form */
.lead-box{position:absolute;left:648px;top:740px;width:201px;height:227px;border:1px solid #d8d8d8;border-radius:4px;background:#fff}
.field{position:absolute;left:13px;width:174px;height:28px;border:2px solid #dadada;border-radius:2px;font-family:"Gelasio",serif;font-style:italic;font-size:10px;color:#666;padding:6px 8px}
.submit{position:absolute;left:11px;top:186px;width:76px;height:24px;border-radius:10px;background:linear-gradient(#eaf7ff,#a9dcf5);border:1px solid #86c7ea;font-family:"Gelasio",serif;font-style:italic;font-weight:700;font-size:12px;color:#1b3f73;text-align:center;line-height:22px}
.offer{position:absolute;left:608px;top:692px}

/* footer */
.footer-rule{position:absolute;left:116px;top:1013px;width:752px;height:1px;background:var(--rule)}
.footer h4{font-size:10px;font-weight:700;color:var(--ink);text-transform:uppercase}
.footer .col{position:absolute;top:1035px;font-size:10px;line-height:15.5px;color:#444;white-space:nowrap}
.footer .col ul{list-style:none;margin-top:9px}
.footer-map{position:absolute;left:288px;top:1040px;width:184px;height:94px;border-radius:40px;background:radial-gradient(ellipse,#eeeeee 0,#f6f6f6 60%,rgba(255,255,255,0) 100%)}
.copyright{position:absolute;left:131px;top:1166px;font-size:10px;color:#444}
.social{position:absolute;left:712px;top:1156px;display:flex;gap:6px}
.social i{width:12px;height:12px;border-radius:2px;background:#9a9a9a}
.social i.first{background:var(--blue-deep)}
</style>
</head>
<body>

<header class="site-header">
  <div class="brand"><span class="brand-mark"></span><span class="brand-name">Bright Path Web Growth</span></div>
  <div class="share"><span>+1</span><span>Share</span><span>Like 0</span></div>
  <nav class="main-nav">
    <svg width="12" height="11" viewBox="0 0 12 11"><path d="M6 0 0 5.5h1.6V11h3V7.5h2.8V11h3V5.5H12z" fill="#555"/></svg>
    <a class="current" href="#">Services</a>
    <a href="#">About Us</a>
    <a href="#">Blog</a>
    <a href="#">Contact</a>
  </nav>
</header>

<section class="hero">
  <div class="hero-photo" role="img" aria-label="Photo of a smiling businessman in a dark suit and striped tie"></div>
  <h1 class="hero-title">We are not about advertising,<br>we are about connecting<br>your customers, and<br><span class="accent">growing your business.</span></h1>
  <p class="hero-copy">Lorem ipsum dolor sit amet consectetuer adipis cing elit. Praesent vestibulum molestie lacus. Aenean nonummy hendrerit mauris. Phasellus porta. Fusce sucipit varius mi. Cum sociis na toque penatibu.</p>
  <div class="btn-more">Learn More <svg width="5" height="7" viewBox="0 0 5 7"><path d="M0 0l5 3.5L0 7z" fill="#222"/></svg></div>
  <div class="slider-bar">
    <div class="dots"><i class="on"></i><i></i><i></i><i></i></div>
    <div class="arrows">‹ ›</div>
  </div>
</section>

<section class="services">
  <div class="service" style="left:115px">
    <div class="service-head">
      <svg width="32" height="38" viewBox="0 0 32 38"><circle cx="16" cy="8" r="8" fill="var(--blue-deep)"/><path d="M1 38V27c0-5 4-8 9-8h12c5 0 9 3 9 8v11z" fill="var(--blue-deep)"/><path d="M16 20l-2 3 2 12 2-12z" fill="#fff"/></svg>
      <h3>Consulting &amp;<br>Strategy Planning</h3>
    </div>
    <p>Magnis d patui entontessce iculu muss ceugiaead a odio. Mor unc avida cursus necucus.</p>
    <a href="#">Learn more...</a>
  </div>
  <div class="service" style="left:315px">
    <div class="service-head">
      <svg width="36" height="36" viewBox="0 0 36 36"><circle cx="22" cy="14" r="11" fill="none" stroke="var(--blue-deep)" stroke-width="4"/><path d="M14 22 3 33" stroke="var(--blue-deep)" stroke-width="6" stroke-linecap="round"/></svg>
      <h3>SEO</h3>
    </div>
    <p>Magnis d patui entontessce iculu muss ceugiaead a odio. Mor unc avida cursus necucus.</p>
    <a href="#">Learn more...</a>
  </div>
  <div class="service" style="left:517px">
    <div class="service-head">
      <svg width="32" height="36" viewBox="0 0 32 36"><path d="M8 2c2 0 3 1 3 3v12h2v-4c2-1 4 0 4 2v2c2-1 4 0 4 2v1c2-1 4 0 4 2v7c0 4-3 7-7 7h-5c-3 0-5-2-7-4l-6-8c-1-2 1-4 3-3l3 3V5c0-2 1-3 2-3z" fill="var(--blue-deep)"/></svg>
      <h3>Pay Per Click</h3>
    </div>
    <p>Magnis d patui entontessce iculu muss ceugiaead a odio. Mor unc avida cursus necucus.</p>
    <a href="#">Learn more...</a>
  </div>
  <div class="service" style="left:717px">
    <div class="service-head">
      <svg width="32" height="36" viewBox="0 0 32 36"><path d="M2 2h20l8 8v24H2z" fill="none" stroke="var(--blue-deep)" stroke-width="3.5"/><path d="M8 26l6-7 4 4 6-8" fill="none" stroke="var(--blue-deep)" stroke-width="3"/></svg>
      <h3>Re-Marketing</h3>
    </div>
    <p>Magnis d patui entontessce iculu muss ceugiaead a odio. Mor unc avida cursus necucus.</p>
    <a href="#">Learn more...</a>
  </div>
</section>

<h2 class="says-title">What People Say:</h2>

<article class="quote" style="left:141px">
  <svg class="mark" width="18" height="14" viewBox="0 0 18 14"><path d="M0 14V7C0 3 2 0 7 0v3C4 3 4 5 4 6h3v8zm10 0V7c0-4 2-7 7-7v3c-3 0-3 2-3 3h3v8z" fill="var(--blue)"/></svg>
  <p>Magnis d patui entontessce iculu muss ceugiaead a odio.</p>
  <p>Mor unc avida cursus necucus a lor isique ci ac sem ultricis pharmet erop sit amet consecueadi scineliris fere ntum dictum mag nadore aliqm leo telluo loapib ueleme ntum vel cnte eu lacusstib.</p>
  <div class="who">- Faucibus L</div>
  <div class="site">HTTP://clientsite.example</div>
</article>
<article class="quote" style="left:389px">
  <svg class="mark" width="18" height="14" viewBox="0 0 18 14"><path d="M0 14V7C0 3 2 0 7 0v3C4 3 4 5 4 6h3v8zm10 0V7c0-4 2-7 7-7v3c-3 0-3 2-3 3h3v8z" fill="var(--blue)"/></svg>
  <p>Magnis d patui entontessce iculu muss ceugiaead a odio.</p>
  <p>Mor unc avida cursus necucus a lor isique ci ac sem ultricis pharmet erop sit amet consecueadi scineliris fere ntum dictum mag nadore aliqm leo telluo loapib ueleme ntum vel cnte eu lacusstib.</p>
  <div class="who">- Faucibus L</div>
  <div class="site">HTTP://clientsite.example</div>
</article>

<form class="lead-box">
  <div class="field" style="top:22px">Full Name:</div>
  <div class="field" style="top:61px">Enter Email:</div>
  <div class="field" style="top:99px">Phone:</div>
  <div class="field" style="top:137px">Website:</div>
  <div class="submit">Submit »</div>
</form>

<svg class="offer" width="260" height="76" viewBox="0 0 260 76">
  <defs>
    <linearGradient id="ribbon" x1="0" y1="0" x2="0" y2="1"><stop offset="0" stop-color="#f7941d"/><stop offset="1" stop-color="#e4560c"/></linearGradient>
    <linearGradient id="seal" x1="0" y1="0" x2="0" y2="1"><stop offset="0" stop-color="#4cb3ee"/><stop offset="1" stop-color="#1466b8"/></linearGradient>
  </defs>
  <path d="M50 12h198l10 23-10 23H50z" fill="url(#ribbon)"/>
  <text x="73" y="33" font-family="Ubuntu, sans-serif" font-weight="700" font-size="11" fill="#fff">STRATEGY SESSIONS,</text>
  <text x="73" y="46" font-family="Ubuntu, sans-serif" font-weight="700" font-size="11" fill="#fff">DOUBLE YOUR WEBSITE LEADS</text>
  <polygon fill="url(#seal)" points="36,2 42,7 49,5 52,12 59,13 59,20 65,24 62,31 66,37 60,42 61,49 54,51 52,58 45,57 40,63 34,59 28,63 24,57 17,57 16,50 9,48 11,41 5,36 10,31 7,24 13,20 13,13 20,12 24,5 31,7"/>
  <text x="36" y="40" text-anchor="middle" transform="rotate(-12 36 34)" font-family="Fredoka, sans-serif" font-weight="600" font-size="19" fill="#fff">FREE</text>
</svg>

<div class="footer-rule"></div>
<footer class="footer">
  <div class="footer-map" role="img" aria-label="Faint dotted world map"></div>
  <div class="col" style="left:131px">
    <h4>Contact Information</h4>
    <ul><li>412 Fenwick Lane Harlow,</li><li>K17 3QT</li></ul>
    <ul style="margin-top:7px"><li>Phone: +1 800 555 01927</li><li>E-mail: mail@brightpath.example</li></ul>
  </div>
  <div class="col" style="left:565px">
    <h4>Quick Links</h4>
    <ul><li>Home</li><li>Services</li><li>About Us</li><li>Blog</li></ul>
  </div>
  <div class="col" style="left:709px">
    <h4>Our Services</h4>
    <ul><li>Consulting &amp; Strategy Planning</li><li>Search Engine Optimisation</li><li>Pay Per Click</li><li>Re-Marketing</li></ul>
  </div>
  <div class="copyright">Copyright © 2012 &nbsp;Bright Path Web Growth, &nbsp;All rights reserved</div>
  <div class="social"><i class="first"></i><i></i><i></i><i></i></div>
</footer>

</body>
</html>
```